front store banner

i need a banner 4'x8' for a print shop store front promoting custom t-shirts, banners, sublimated mugs, business cards, car magnets, window decals, postcards and passport pictures

```html
<!DOCTYPE html>
<html lang="en">
<head>
<meta charset="utf-8">
<title>Tall Wave Apparel – Storefront Banner</title>
<link rel="stylesheet" href="https://fonts.googleapis.com/css2?family=Montserrat:wght@800&family=Questrial&display=swap">
<style>
  :root {
    --bg-page: #1a1410;
    --scene-center: #cdbfa6;
    --scene-mid: #8a7350;
    --scene-green: #6f7d2c;
    --scene-dark: #2c2415;
    --glow-pink: #ff8fb0;
    --glow-red: #d8324a;
    --name-white: #fbf6ef;
    --bar-dark: #151212;
    --bar-mid: #3a3434;
    --bar-edge: #c9c3c0;
    --box-fill: rgba(28, 20, 22, 0.82);
    --box-edge: rgba(255, 255, 255, 0.55);
    --text-gold: #ffc04a;
    --text-orange: #ff8a2e;
    --text-red: #ff4a3a;
    --frame-line: rgba(230, 255, 150, 0.55);
  }
  * { box-sizing: border-box; margin: 0; padding: 0; }
  html, body {
    width: 1200px; height: 601px; overflow: hidden;
    background: var(--bg-page);
  }
  .banner {
    position: relative; width: 1200px; height: 601px; overflow: hidden;
  }
  .banner__scene {
    position: absolute; inset: 0;
    background:
      radial-gradient(ellipse 420px 160px at 80px 420px, rgba(255,160,200,0.85), transparent 70%),
      radial-gradient(ellipse 420px 160px at 1130px 420px, rgba(255,160,200,0.8), transparent 70%),
      radial-gradient(ellipse 700px 200px at 600px 600px, rgba(216,50,74,0.75), transparent 75%),
      radial-gradient(ellipse 520px 300px at 600px 230px, var(--scene-center), transparent 80%),
      linear-gradient(90deg, var(--scene-green) 0%, var(--scene-mid) 18%, var(--scene-mid) 82%, var(--scene-green) 100%);
  }
  .banner__frame {
    position: absolute; inset: 7px;
    border: 1.5px solid var(--frame-line);
    pointer-events: none;
  }
  .brand {
    position: absolute; left: 0; right: 0; top: 40px;
    text-align: center;
    font-family: "Montserrat", sans-serif;
    font-weight: 800;
    color: var(--name-white);
    line-height: 1;
  }
  .brand__name { display: block; font-size: 112px; letter-spacing: 1px; }
  .brand__kind { display: block; font-size: 104px; letter-spacing: 6px; margin-top: 30px; }
  .service-bar {
    position: absolute; left: 207px; top: 377px; width: 818px; height: 54px;
    border-radius: 8px;
    border: 2px solid var(--bar-edge);
    background: linear-gradient(180deg, var(--bar-mid), var(--bar-dark));
    display: flex; align-items: center; justify-content: center;
    font-family: "Montserrat", sans-serif; font-weight: 800;
    font-size: 40px; letter-spacing: 7px; color: var(--name-white);
  }
  .offer-box {
    position: absolute; left: 133px; top: 445px; width: 955px; height: 127px;
    border-radius: 4px;
    border: 1.5px solid var(--box-edge);
    background: var(--box-fill);
    display: flex; flex-direction: column; justify-content: center; align-items: center;
    font-family: "Questrial", sans-serif;
    font-size: 26px; line-height: 38px; letter-spacing: 0.5px;
    text-transform: uppercase;
  }
  .offer-box__line--1 { color: var(--text-gold); }
  .offer-box__line--2 { color: var(--text-orange); }
  .offer-box__line--3 { color: var(--text-red); }
</style>
</head>
<body>
  <main class="banner">
    <div class="banner__scene" role="img" aria-label="Bamboo stalks and palm fronds over a warm aged backdrop, with pink lightning glow along the bottom"></div>
    <div class="banner__frame"></div>

    <h1 class="brand">
      <span class="brand__name">Tall Wave</span>
      <span class="brand__kind">APPAREL</span>
    </h1>

    <div class="service-bar">/////PRINTING SHOP</div>

    <p class="offer-box">
      <span class="offer-box__line--1">Promoting custom t-shirts, banners, sublimated</span>
      <span class="offer-box__line--2">mugs, business cards, car magnets, window decals,</span>
      <span class="offer-box__line--3">postcards and passport pictures</span>
    </p>
  </main>
</body>
</html>
```